Tall Birch Path newsletter - Mail Chimp

Tall Birch Path - Empowering Life Coach needs Mail Chimp Newsletter Template. This is a newsletter I will send out monthly to current clients and prospective clients to offer (hopefully) inspiring and uplifting content AND to give info and dates of my upcoming workshops and retreats.

I have attached a word document with all of the different sections of the mail chimp template I would like to have - and hte actual content for the first newsletter.

I'd like to look uplifting, fun, inspiring.

I also need it to be easy for me to use to update in the future :)

Target Market(s)

Women - moms

Industry/Entity Type

Life Coaching

Requirements
Nice to have
• Color theme to match my "Tall Birch Path" logo

```html
<!DOCTYPE html>
<html lang="en">
<head>
<meta charset="utf-8">
<title>Tall Birch Path Newsletter</title>
<link href="https://fonts.googleapis.com/css2?family=Arimo:ital,wght@0,400;0,700;1,400&family=Chewy&family=Open+Sans:wght@400;600&display=swap" rel="stylesheet">
<style>
:root{
  --purple:#6a2c91;
  --teal:#3ab0d1;
  --teal-dark:#2a93b5;
  --green:#8cc63f;
  --sky:#cfe6f5;
  --ink:#222;
  --grey:#c9c9c9;
  --white:#fff;
}
*{box-sizing:border-box;margin:0;padding:0}
html,body{width:1200px;height:4186px;overflow:hidden;background:var(--white)}
body{font-family:"Arimo",Arial,sans-serif;color:var(--ink);font-size:19px;line-height:1.36;position:relative}
.wrap{padding:0 64px}

/* header */
.masthead{position:relative;height:1150px;background:linear-gradient(180deg,var(--sky) 0,#e4f1fa 60%,#fff 100%)}
.masthead-brush{position:absolute;left:0;top:880px;width:1200px;height:260px}
.brand{position:absolute;left:56px;top:90px;display:flex;align-items:center;gap:18px}
.brand-dot{width:46px;height:46px;border-radius:50%;background:var(--purple)}
.brand-name{font-family:"Arimo",sans-serif;font-weight:700;font-size:54px;color:var(--purple);line-height:1}
.hero{position:absolute;left:380px;top:-40px;width:840px;height:1120px}

/* letter */
.letter{padding-top:40px}
.letter p{margin-bottom:18px}
.sign{margin-top:42px}
.rule-purple{height:8px;background:var(--purple);margin:38px 0 30px}
.section-title{font-weight:700;font-size:38px;color:var(--purple);text-align:center;letter-spacing:.5px}
.rule-grey{height:2px;background:var(--grey);margin:16px 0 24px}

/* tips */
.building{display:flex;gap:40px}
.building-text{flex:1}
.sub{font-weight:700;margin-bottom:16px}
.building-text p{margin-bottom:14px}
.hands-photo{width:520px;height:300px;border:10px solid var(--purple);background:linear-gradient(160deg,#f7d27a,#e89a3a 55%,#8a4a1c);flex:none;margin-top:32px}
.bullets{list-style:none;margin:18px 0 16px}
.bullets li{margin-bottom:14px}
.bullets li::before{content:"»";margin-right:14px}
.prompt-pair{display:flex;gap:44px;margin-top:46px}
.prompt{position:relative;flex:1;height:360px}
.prompt::before{content:"";position:absolute;left:18px;top:18px;right:-18px;bottom:-18px;background:var(--green)}
.prompt-inner{position:relative;height:100%;background:var(--teal);color:var(--white);padding:42px 40px}
.prompt h3{font-size:22px;font-weight:700;margin-bottom:12px;line-height:1.3}
.prompt p{font-style:italic;font-size:20px;line-height:1.3}
.challenge{display:flex;gap:8px;margin-top:60px;height:308px}
.challenge-box{width:520px;background:var(--green);padding:60px 30px 0 30px;font-weight:700;font-size:25px;line-height:1.3;color:#203010}
.challenge-box p{margin-bottom:22px}
.quote-card{height:100%}
.quote-dark{width:205px;background:linear-gradient(180deg,#1e2a36,#34465a)}
.quote-light{flex:1;background:linear-gradient(180deg,#d9d4d0,#bdb3ae)}

/* books & events */
.rule-soft{height:2px;background:#e0e0e0;margin:58px 0 18px}
.label{font-weight:700;color:var(--purple);margin-bottom:12px}
.label-teal{color:var(--teal)}
.rule-teal{height:6px;background:var(--teal);margin:16px 0 18px}
.partner{display:flex;flex-direction:column;align-items:center;margin:40px 0 26px}
.partner-mark{width:60px;height:60px;border-radius:50%;background:var(--teal)}
.partner-name{font-family:"Open Sans",sans-serif;font-weight:600;font-size:30px;color:var(--teal);letter-spacing:3px;margin-top:10px}
.moms-title{font-family:"Chewy",cursive;font-size:50px;color:var(--purple);text-align:center;line-height:1.1;margin-bottom:16px}
.moms-title span{color:var(--green)}

/* workshop */
.workshop{position:absolute;left:0;top:3650px;width:1200px;height:536px}
.workshop-brush{position:absolute;left:0;top:0;width:1200px;height:50px}
.workshop-body{position:absolute;left:64px;top:62px;width:720px}
.workshop-title{font-family:"Open Sans",sans-serif;font-size:38px;color:var(--teal-dark);line-height:1}
.date-band{margin-top:14px;width:600px;height:78px;background:var(--teal);color:var(--white);font-weight:700;font-size:44px;line-height:78px;padding-left:26px;clip-path:polygon(0 0,100% 0,92% 100%,0 100%)}
.time-band{margin-left:60px;width:500px;height:60px;background:var(--green);color:var(--white);font-weight:700;font-size:38px;line-height:60px;padding-left:70px;clip-path:polygon(0 0,100% 0,94% 100%,0 100%)}
.venue{margin-top:26px;font-size:19px}
.venue strong{color:var(--purple)}
.wish-list{list-style:none;margin-top:14px;font-size:19px}
.wish-list li{line-height:1.32}
.wish-list li::before{content:"|";color:var(--purple);margin-right:10px}
.wish-list .hl{color:var(--purple)}
.quote-photo{position:absolute;right:60px;top:60px;width:330px;height:300px;background:linear-gradient(135deg,#3a3a3a,#8a8a8a 55%,#d8d8d8)}
.footer-band{position:absolute;left:0;bottom:0;width:1200px;height:120px}
.footer-text{position:absolute;left:64px;bottom:18px;width:1070px;font-size:16px;color:#1a2a3a;line-height:1.35}
</style>
</head>
<body>

<header class="masthead">
  <svg class="masthead-brush" viewBox="0 0 1200 260" preserveAspectRatio="none" aria-hidden="true">
    <path d="M0 120 C200 80 420 150 640 110 C820 80 1000 140 1200 100 L1200 260 L0 260 Z" fill="#7cc4e6" opacity=".55"/>
    <path d="M0 170 C240 140 500 200 760 160 C940 135 1080 175 1200 150 L1200 260 L0 260 Z" fill="#fff"/>
  </svg>
  <div class="brand"><span class="brand-dot"></span><span class="brand-name">Tall Birch Path</span></div>
  <svg class="hero" viewBox="0 0 840 1120" aria-hidden="false">
    <polygon points="80,330 420,120 780,330 780,760 420,960 80,760" fill="none" stroke="var(--teal)" stroke-width="8" transform="translate(-120,80)"/>
    <polygon points="80,330 420,120 780,330 780,760 420,960 80,760" fill="none" stroke="var(--purple)" stroke-width="8" transform="translate(40,100)"/>
    <defs>
      <linearGradient id="heroFill" x1="0" y1="0" x2="1" y2="1">
        <stop offset="0" stop-color="#3fb3de"/>
        <stop offset=".55" stop-color="#f2cf3a"/>
        <stop offset="1" stop-color="#c98a5a"/>
      </linearGradient>
    </defs>
    <polygon role="img" aria-label="Photo of the coach in a cap relaxing on a yellow float in a pool" points="70,240 420,40 800,240 800,780 420,980 70,780" fill="url(#heroFill)"/>
  </svg>
</header>

<section class="wrap letter">
  <p>Hello Friends!</p>
  <p>I am excited to (hopefully) add a little love to your in-box with this newsletter. I love connecting with moms and helping them find tools to make their lives happier, more intentional, and more fun and this is a new way to do that!</p>
  <p>If you don't know me well, I am a certified Open Horizons Trainer and I lead coaching groups for moms. My OH workshops and Empowered Moms Coaching Group have the goal of fostering connections between amazing women and empowering moms with tools to build lives they are enthusiastic about living, on purpose – and that will be the goal of this newsletter, as well!</p>
  <p>I hope you find something useful and helpful and enjoy receiving this info (and if not, feel free to unsubscribe and my feelings will not be hurt!</p>
  <p class="sign">With love,<br><strong>Dana</strong></p>
  <div class="rule-purple"></div>
  <h2 class="section-title">TALL BIRCH PATH TIPS &amp; TOOLS</h2>
  <div class="rule-grey"></div>

  <div class="building">
    <div class="building-text">
      <p class="sub">Building Happiness</p>
      <p>I firmly believe that thinking about your happiness is important and that happiness itself is a worthwhile goal! If you think about all the things you focus on in your life and all the goals you set for yourself, all of those things are leading you toward feeling happier. Happiness, in the end, is the ultimate goal.</p>
      <p>Of course, what makes each person happy is totally different – and that's awesome and one part of what makes life fun and exciting! Many happiness experts and authors note that the key ingredients in our lives that will make us happier are pursuing 2 categories:</p>
    </div>
    <div class="hands-photo" role="img" aria-label="Photo of hands forming a heart shape against a golden sunset"></div>
  </div>
  <ul class="bullets">
    <li>things that bring us pleasure (positive emotions) <em>and</em></li>
    <li>things that bring us meaning &amp; fulfillment</li>
  </ul>
  <p>Give yourself a minute to think about (it's extra powerful if you write it down!) what makes YOU happy.</p>

  <div class="prompt-pair">
    <div class="prompt"><div class="prompt-inner">
      <h3>What are things that make you feel happy / provide you with pleasure (little and big things!)?</h3>
      <p>For me: joking &amp; laughing with my kids &amp; husband, petting with my dog, sitting with a soft blanket and a book, my first sip of coffee in the morning, walking in nature, travelling, scuba diving, exercise classes, making my friends laugh.</p>
    </div></div>
    <div class="prompt"><div class="prompt-inner">
      <h3>What are things that are meaningful to you / make you feel fulfilled (little and big things!)?</h3>
      <p>For me: teaching Open Horizons workshops, spending quality time with my family, making gratitude lists, volunteering, leading moms' coaching groups, making my kids breakfast.</p>
    </div></div>
  </div>

  <div class="challenge">
    <div class="challenge-box">
      <p>How could you add more of those things that bring you happiness to your days?</p>
      <p>Try to add 1 or 2 of those things per week and see how your happiness increases! You are worth it!</p>
    </div>
    <div class="quote-card quote-dark" role="img" aria-label="Quote card about designing happiness for the present"></div>
    <div class="quote-card quote-light" role="img" aria-label="Quote card about happiness found in the simplest of things"></div>
  </div>

  <div class="rule-soft"></div>
  <p class="label">Empowering Books:</p>
  <p>I love to read uplifting, inspiring material. Each newsletter, I'll suggest a few books that I've enjoyed!<br>
  The Joy Experiment by Margaret Linwood<br>
  You Are Unstoppable. How to Quiet Your Doubts and Start Living a Brilliant Life" by Clara Weston</p>
  <div class="rule-teal"></div>
  <p class="label label-teal">Upcoming Events:</p>
  <p>I lead an Open Horizons Workshop 2-3 times per year. The next one is coming up in September / October. More details to come – but here is a little info…</p>

  <div class="partner"><span class="partner-mark"></span><span class="partner-name">OPEN HORIZONS</span></div>
  <h2 class="moms-title">Moms - <span>Back to School, Back to You!</span></h2>
  <p>In September, the kids will be going back to school and you can spend time focusing on YOU. Let this be the year where you take time to focus on yourself so that you can feel amazing, focused, fulfilled, purposeful, and happier! Take the time to learn some simple tools to help you live a life you love, deliberately, instead of just juggling what comes at you and juggling your to-do list. In this workshop, you will be empowered to build a life you love.</p>
</section>

<section class="workshop">
  <svg class="workshop-brush" viewBox="0 0 1200 50" preserveAspectRatio="none" aria-hidden="true">
    <path d="M0 14 C150 4 300 22 480 10 C700 0 900 24 1200 8 L1200 34 C980 46 760 28 540 40 C320 50 160 32 0 44 Z" fill="var(--teal)"/>
  </svg>
  <div class="workshop-body">
    <h2 class="workshop-title">3 MORNING WORKSHOP</h2>
    <div class="date-band">SEP. 27, – OCT. 4 &amp; 11</div>
    <div class="time-band">09:30 – 12:30</div>
    <p class="venue">Dana's home in Maple Ridge<br><strong>Interested?</strong> Email me: <strong>dana@tallbirchpath.com</strong></p>
    <ul class="wish-list">
      <li>Enjoy the rest of Summer Break!</li>
      <li>Savor each amazing day!</li>
      <li class="hl">How can you add a little more HAPPY to your August?</li>
      <li>Make the choice and do it!</li>
    </ul>
  </div>
  <div class="quote-photo" role="img" aria-label="Black and white quote card about happiness being the key to life"></div>
  <svg class="footer-band" viewBox="0 0 1200 120" preserveAspectRatio="none" aria-hidden="true">
    <path d="M0 30 C180 10 360 36 560 18 C780 0 980 30 1200 12 L1200 120 L0 120 Z" fill="#6fbbe0"/>
  </svg>
  <p class="footer-text">This email is sent by Brightline Mail Ltd on behalf of <strong>CLIENT NAME</strong>. We only send emails that we feel are relevant to you. You can unsubscribe from future emails from this client by clicking here.</p>
</section>

</body>
</html>
```